Label Design for 2x Chutney Products

We need a label design for 2x Chutney Products.
Zintara Chutney - Red Chili
Zintara Chutney - Green Chili & Coriander
See attached pictures. This is just sample pictures so you get an impression of the product and the colors. Both labels to have as title the generic name "Zintara Chutney" and then added either Red Chili or Green Chili & Coriander. The different terms needs to be good readable and can differ in font/color/size, or in the same style if this makes more sense from design point (as I am not a designer). The labels later on need to be editable in the way that the ingredient list, nutrition list, basis company and production information can be added. If this needs to be done directly and cannot be edited later on please let know. Editable design related the additional text also would be good as the additional information need to be added in different languages (Dutch. German and perhaps French). No clue how this is to be implemented but looking forward to receive some input/solutions on this.
I already had a project to create the company logo. I consider this logo to be used as the product logo and not the company logo. A different company logo later on can be designed from new. This logo is here attached. Either to work with this logo and use it as product logo (perhaps revise the colors) and add the product description or create a new logo for the product from scratch if you feel too. The logo itself should be easily readable for the product name/description and the colors appealing to such product and of course customers.
Please contact if any clarification needed. Thanks in advance for your efforts and ideas for this project.

Industry/Entity Type

Food

Other font styles liked:
• Asian Touch

Requirements
Nice to have
• If possible "simply" editable for text fields in order to add/revise the ingredient list, nutrition list, revise to different languages.

```html
<!DOCTYPE html>
<html lang="en">
<head>
<meta charset="utf-8">
<title>Zintara Chutney – Label Set</title>
<link rel="stylesheet" href="https://fonts.googleapis.com/css2?family=Montserrat:wght@600;700&family=Staatliches&display=swap">
<style>
  :root {
    --bg: #ececec;
    --paper: #efe7da;
    --ink: #1c1c1c;
    --chili-red: #c8161d;
    --frame-red: #e0353a;
    --chili-green: #6bb52a;
    --art-red-light: #e8564a;
    --art-red-dark: #a5121a;
    --art-green-light: #8fd04a;
    --art-green-dark: #3f8a1e;
    --sketch-red: #d9a39a;
    --sketch-green: #b9d79a;
  }
  * { box-sizing: border-box; margin: 0; padding: 0; }
  html, body { width: 1200px; height: 800px; overflow: hidden; }
  body {
    background: var(--bg);
    font-family: "Montserrat", Arial, sans-serif;
    display: flex;
    align-items: center;
    justify-content: center;
    gap: 40px;
  }
  .label {
    width: 540px;
    height: 360px;
    display: flex;
    background: #fff;
    box-shadow: 0 10px 30px rgba(0,0,0,0.12);
  }
  .label-art { width: 100px; flex: none; }
  .label--red .label-art { background: linear-gradient(160deg, var(--art-red-light), var(--art-red-dark) 55%, var(--art-red-light)); }
  .label--green .label-art { background: linear-gradient(160deg, var(--art-green-light), var(--art-green-dark) 55%, var(--art-green-light)); }
  .label-panel {
    position: relative;
    flex: 1;
    background: var(--paper);
    display: flex;
    flex-direction: column;
    align-items: center;
    padding: 40px 30px 30px;
  }
  .panel-frame { position: absolute; inset: 0; width: 100%; height: 100%; }
  .panel-frame path { fill: none; stroke: var(--frame-red); }
  .brand { display: flex; align-items: center; gap: 14px; position: relative; }
  .brand-dot { width: 54px; height: 54px; border-radius: 50%; background: var(--chili-red); }
  .label--green .brand-dot { background: var(--chili-green); }
  .brand-name {
    font-weight: 700;
    font-size: 24px;
    line-height: 1;
    letter-spacing: 1px;
    color: var(--ink);
    text-transform: uppercase;
  }
  .sketch {
    position: relative;
    margin-top: 16px;
    width: 110px;
    height: 46px;
    border-radius: 30px;
  }
  .label--red .sketch { background: linear-gradient(90deg, transparent, var(--sketch-red), transparent); }
  .label--green .sketch { background: linear-gradient(90deg, transparent, var(--sketch-green), transparent); }
  .product-line {
    position: relative;
    margin-top: 14px;
    font-weight: 600;
    font-size: 22px;
    letter-spacing: 1px;
    color: var(--ink);
    text-transform: uppercase;
  }
  .variant {
    position: relative;
    margin-top: 6px;
    font-family: "Staatliches", Impact, sans-serif;
    text-align: center;
    line-height: 0.95;
    text-transform: uppercase;
  }
  .label--red .variant { color: var(--chili-red); font-size: 70px; }
  .label--green .variant { color: var(--chili-green); font-size: 46px; }
</style>
</head>
<body>

  <section class="label label--red">
    <div class="label-art" role="img" aria-label="Illustrated red chili peppers"></div>
    <div class="label-panel">
      <svg class="panel-frame" viewBox="0 0 340 360" preserveAspectRatio="none" aria-hidden="true">
        <path stroke-width="1.5" d="M24 12 H316 V24 H328 V336 H316 V348 H24 V336 H12 V24 H24 Z"/>
        <path stroke-width="1" d="M30 18 H310 V30 H322 V330 H310 V342 H30 V330 H18 V30 H30 Z"/>
      </svg>
      <div class="brand">
        <span class="brand-dot"></span>
        <span class="brand-name">Velora<br>Foods</span>
      </div>
      <div class="sketch" role="img" aria-label="Line sketch of red chili peppers"></div>
      <p class="product-line">Zintara Chutney</p>
      <h1 class="variant">Red Chili</h1>
    </div>
    <div class="label-art" role="img" aria-label="Illustrated red chili peppers"></div>
  </section>

  <section class="label label--green">
    <div class="label-art" role="img" aria-label="Illustrated green chili peppers"></div>
    <div class="label-panel">
      <svg class="panel-frame" viewBox="0 0 340 360" preserveAspectRatio="none" aria-hidden="true">
        <path stroke-width="1.5" d="M24 12 H316 V24 H328 V336 H316 V348 H24 V336 H12 V24 H24 Z"/>
        <path stroke-width="1" d="M30 18 H310 V30 H322 V330 H310 V342 H30 V330 H18 V30 H30 Z"/>
      </svg>
      <div class="brand">
        <span class="brand-dot"></span>
        <span class="brand-name">Velora<br>Foods</span>
      </div>
      <div class="sketch" role="img" aria-label="Line sketch of coriander leaves and green chilies"></div>
      <p class="product-line">Zintara Chutney</p>
      <h1 class="variant">Green Chili<br>Coriander</h1>
    </div>
    <div class="label-art" role="img" aria-label="Illustrated green chili peppers"></div>
  </section>

</body>
</html>
```